Super elegant, crisp & clean Business card design required

We recently upgraded our branding - which is on our website - tavorelstudio.com

I would like a simple, yet elegant, clean business card design please.

The font of my logo is Cinzel - and because of the natural colour - it's best to have this on a black background.

I would like to have the back of the business card - with simply my logo.

PLEASE DO NOT SUBMIT A COMPLICATED / UNCLEAN DESIGN

Industry/Entity Type

Business

Contact Information for Business Card

Dalvik Ostrander Photography

Font styles to use
Other font styles liked:
• Cinzel

Requirements
Must have
• A backpage with nothing but my logo
• Simple design - stands out
Should not have
• Colour that dont align with my logo
• Over complicated '/ non symmetrical design

```html
<!DOCTYPE html>
<html lang="en">
<head>
<meta charset="utf-8">
<title>Dalvik Ostrander Photography – Business Card</title>
<link rel="stylesheet" href="https://fonts.googleapis.com/css2?family=Cinzel:wght@400&display=swap">
<style>
  :root {
    --backdrop: #d6d6d6;
    --card: #0c0c0c;
    --bronze: #7a6552;
    --bronze-soft: #5e4e40;
  }
  html, body {
    margin: 0;
    padding: 0;
    width: 1200px;
    height: 781px;
    overflow: hidden;
    background: var(--backdrop);
  }
  .canvas {
    position: relative;
    width: 1200px;
    height: 781px;
  }
  .card {
    position: absolute;
    left: 358px;
    width: 452px;
    height: 251px;
    background: var(--card);
    font-family: "Cinzel", serif;
    color: var(--bronze);
    text-align: center;
  }
  .card--front { top: 103px; }
  .card--back  { top: 408px; }

  .brand-dot {
    position: absolute;
    left: 50%;
    width: 18px;
    height: 18px;
    margin-left: -10px;
    border: 1px solid var(--bronze);
    border-radius: 50%;
  }
  .card--front .brand-dot { top: 68px; }
  .card--back  .brand-dot { top: 98px; }

  .brand-name {
    position: absolute;
    left: 0;
    right: 0;
    margin: 0;
    font-weight: 400;
    font-size: 17px;
    letter-spacing: 0.5px;
    line-height: 1;
  }
  .brand-name .brand-sub {
    display: block;
    margin-top: 3px;
    font-size: 8px;
    letter-spacing: 4.5px;
    padding-left: 4.5px;
  }
  .card--front .brand-name { top: 124px; }
  .card--back  .brand-name { top: 164px; }

  .contact {
    position: absolute;
    left: 0;
    right: 0;
    top: 180px;
    margin: 0;
    padding: 0;
    list-style: none;
    font-size: 10px;
    line-height: 14.5px;
    color: var(--bronze-soft);
  }
</style>
</head>
<body>
<main class="canvas">
  <section class="card card--front" aria-label="Card front">
    <span class="brand-dot" aria-hidden="true"></span>
    <h1 class="brand-name">Dalvik Ostrander<span class="brand-sub">Photography</span></h1>
    <ul class="contact">
      <li>Tel: 07900 418263</li>
      <li>Email: info@tavorelstudio.com</li>
      <li>Web: www.tavorelstudio.com</li>
    </ul>
  </section>

  <section class="card card--back" aria-label="Card back">
    <span class="brand-dot" aria-hidden="true"></span>
    <h2 class="brand-name">Dalvik Ostrander<span class="brand-sub">Photography</span></h2>
  </section>
</main>
</body>
</html>
```